Thistleby's Organic's. I make and sell organic bath & body products. Nourishing bath & body products. Products are soaps, scrubs, lip balms, bath salts, baby & mother products (belly balm, nipple balm, diaper balm, baby bath soak, chest rub,) . I use botanical and or herbs in all my recipes. I create my own recipes. I like muted colors...but I would like something that will get your attention. I like the colors green and brown, but open to any other colors. I would also like to get information about labels (different sizes for my products) I do like the pasley print and maybe even a cute owl.

Target Market(s)

women, pregnant and nursing women, women with children and men

Industry/Entity Type

Baby

Contact Information for Business Card

Rhoda Quillmore
527-614-2870,rquillmore@lumaweb.net
rquillmore@lumaweb.net

Font styles to use
Other font styles liked:
• bree

Requirements
Must have
• Thistleby's Organic's, nourishing bath & body products. It needs to get a person attention. I would like to see cards that are hip and fun. I would also like to view cards that are classy. I do like muted colors but I do have an open mind (use any color you think would be right) So far a lot of the cards have had leaves....I really do not like that design.
Nice to have
• ???pasley in the background ?cute owl
Should not have
• leaves

```html
<!DOCTYPE html>
<html lang="en">
<head>
<meta charset="utf-8">
<title>Thistleby's Organic's — Business Card</title>
<link rel="stylesheet" href="https://fonts.googleapis.com/css2?family=Cinzel:wght@500;700&family=Libre+Baskerville&display=swap">
<style>
  :root {
    --page: #ffffff;
    --paper-light: #e9c99a;
    --paper-mid: #d9b07a;
    --paper-dark: #b98a55;
    --ink: #2e1e16;
    --ornament: #7a5f52;
    --green-dark: #3b6a1c;
    --green-soft: #5f9a34;
  }
  * { margin: 0; padding: 0; box-sizing: border-box; }
  html, body { width: 1200px; height: 702px; overflow: hidden; background: var(--page); }
  .card {
    position: absolute; left: 58px; top: 58px; width: 1086px; height: 587px;
    overflow: hidden;
    background: radial-gradient(ellipse at 45% 40%, var(--paper-light) 0%, var(--paper-mid) 60%, var(--paper-dark) 100%);
    color: var(--ink);
  }
  .green-swoosh { position: absolute; inset: 0; width: 100%; height: 100%; }
  .business-name {
    position: absolute; left: 0; right: 0; top: 70px; text-align: center;
    font-family: "Cinzel", serif; font-weight: 500; font-size: 57px; letter-spacing: 3px;
  }
  .tagline {
    position: absolute; left: 0; right: 0; top: 170px; height: 50px;
    font-family: "Libre Baskerville", serif; font-size: 25px;
  }
  .tagline .rule { position: absolute; top: 42px; height: 3px; background: var(--ink); }
  .tagline .rule-left { left: 71px; width: 438px; }
  .tagline .rule-right { left: 554px; width: 466px; }
  .tagline .part-left { position: absolute; right: 584px; top: 10px; }
  .tagline .part-right { position: absolute; left: 558px; top: 10px; }
  .tagline .amp { position: absolute; left: 513px; top: 18px; font-size: 32px; }
  .person-name {
    position: absolute; left: 0; right: 0; top: 278px; text-align: center;
    font-family: "Cinzel", serif; font-weight: 700; font-size: 30px;
  }
  .ornament {
    position: absolute; left: 500px; top: 364px; width: 84px; height: 150px;
    background: radial-gradient(ellipse at center, var(--ornament) 0%, var(--ornament) 35%, transparent 70%);
  }
  .contact {
    position: absolute; left: 30px; top: 406px; list-style: none;
    font-family: "Cinzel", serif; font-weight: 700;
  }
  .contact li { display: flex; align-items: center; gap: 16px; height: 38px; }
  .contact .phone { font-size: 30px; letter-spacing: 1px; }
  .contact .email { font-size: 25px; }
  .contact svg { width: 26px; height: 26px; fill: var(--ornament); flex: none; }
</style>
</head>
<body>
  <div class="card">
    <svg class="green-swoosh" viewBox="0 0 1086 587" preserveAspectRatio="none" role="img" aria-label="Green swoosh band along the bottom edge">
      <defs>
        <linearGradient id="swoosh-fill" x1="0" y1="0" x2="1" y2="1">
          <stop offset="0" stop-color="var(--green-dark)"/>
          <stop offset="1" stop-color="var(--green-soft)"/>
        </linearGradient>
      </defs>
      <path fill="url(#swoosh-fill)" d="M0,435 C140,530 330,580 540,578 C760,575 880,290 1086,238 L1086,587 L0,587Z"/>
    </svg>

    <h1 class="business-name">Thistleby's Organic's</h1>

    <div class="tagline">
      <span class="rule rule-left"></span>
      <span class="rule rule-right"></span>
      <span class="part-left">organic bath</span>
      <span class="amp">&amp;</span>
      <span class="part-right">body products</span>
    </div>

    <p class="person-name">Rhoda Quillmore</p>

    <div class="ornament" role="img" aria-label="Decorative brown flower ornament"></div>

    <ul class="contact">
      <li class="phone">
        <svg viewBox="0 0 24 24" aria-hidden="true"><path d="M6.6 2.5l2.6 4.2-1.8 1.9c.9 2.4 2.6 4.6 4.8 6l2-1.6 4.1 2.6-1.3 3.6c-.5 1-1.6 1.4-2.6 1.1C8.7 18.7 4.3 13.5 3 6.8c-.2-1 .4-2 1.3-2.5z"/><path d="M15 4.5a5 5 0 0 1 4.5 4.5h-1.6A3.4 3.4 0 0 0 15 6.1zM15 1a8.5 8.5 0 0 1 8 8h-1.6A6.9 6.9 0 0 0 15 2.6z"/></svg>
        <span>527-614-2870</span>
      </li>
      <li class="email">
        <svg viewBox="0 0 24 24" aria-hidden="true"><path d="M2 5h20v14H2z"/><path d="M2 5l10 8 10-8" fill="none" stroke="#e0bd8a" stroke-width="1.6"/></svg>
        <span>rquillmore@lumaweb.net</span>
      </li>
    </ul>
  </div>
</body>
</html>
```